Business Card for Lorena Whitfield

Name: Lorena Whitfield
Title: Realtor
Email: Lorena@LorenaWhitfieldRE.com
Phone: 480-555-0137

On the front of the business card, I would like the photo, the contact information and the Lorena Whitfield Logo. The backside is required to have the Broker logo and the required logos. Please use the colors from the logo design. Our company has a classy, professional look.

```html
<!DOCTYPE html>
<html lang="en">
<head>
<meta charset="utf-8">
<title>Lorena Whitfield Real Estate – Business Card</title>
<link href="https://fonts.googleapis.com/css2?family=Cinzel:wght@500&family=Tinos:ital@0;1&family=Open+Sans:wght@700&display=swap" rel="stylesheet">
<style>
  :root {
    --backdrop: #6a6668;
    --paper: #f7f7f6;
    --charcoal: #484849;
    --crimson: #a61e34;
    --ink: #3d3d3f;
    --white: #ffffff;
    --photo-light: #b9b9b9;
    --photo-dark: #3a3a3b;
  }
  * { margin: 0; padding: 0; box-sizing: border-box; }
  html, body { width: 1200px; height: 1200px; overflow: hidden; }
  body { background: var(--backdrop); position: relative; }

  .card {
    position: absolute;
    width: 594px;
    height: 348px;
    border-radius: 18px;
    overflow: hidden;
  }
  .card--front { left: 298px; top: 200px; background: var(--paper); }
  .card--back { left: 292px; top: 637px; background: var(--charcoal); }

  /* brand lockup */
  .brand {
    position: absolute;
    display: flex;
    align-items: center;
    gap: 14px;
    font-family: "Cinzel", serif;
    font-weight: 500;
    letter-spacing: 0.5px;
    white-space: nowrap;
  }
  .brand__mark { width: 34px; height: 34px; flex: none; }
  .card--front .brand {
    left: 0; right: 0; top: 100px;
    justify-content: center;
    font-size: 33px;
    color: var(--crimson);
  }
  .card--front .brand__mark { background: var(--crimson); }
  .card--back .brand {
    left: 25px; top: 52px;
    gap: 12px;
    font-size: 24px;
    color: var(--white);
  }
  .card--back .brand__mark { width: 28px; height: 28px; background: var(--white); }

  /* front contact */
  .contact {
    position: absolute;
    left: 0; right: 0;
    display: flex;
    justify-content: center;
    align-items: center;
    gap: 8px;
    font-family: "Tinos", serif;
    font-size: 17px;
    color: var(--ink);
  }
  .contact--phone { top: 192px; }
  .contact--web { top: 220px; }
  .contact svg { width: 14px; height: 14px; fill: var(--crimson); flex: none; }
  .contact__spacer { width: 10px; }

  .tagline-band {
    position: absolute;
    left: 0; bottom: 0;
    height: 39px;
    background: var(--crimson);
    color: var(--white);
    font-family: "Tinos", serif;
    font-size: 16px;
    display: flex;
    align-items: center;
    justify-content: center;
  }
  .card--front .tagline-band { width: 100%; }
  .card--back .tagline-band { width: 331px; height: 38px; }

  /* back details */
  .tab {
    position: absolute;
    left: -10px; top: 130px;
    width: 20px; height: 42px;
    border-radius: 50%;
    background: var(--crimson);
  }
  .agent-name {
    position: absolute;
    left: 27px; top: 124px;
    font-family: "Cinzel", serif;
    font-weight: 500;
    font-size: 22px;
    color: var(--white);
    white-space: nowrap;
  }
  .agent-title {
    position: absolute;
    left: 28px; top: 155px;
    font-family: "Tinos", serif;
    font-style: italic;
    font-size: 16px;
    color: #e6e6e6;
  }
  .agent-phone {
    position: absolute;
    left: 27px; top: 194px;
    display: flex;
    align-items: center;
    gap: 10px;
    font-family: "Open Sans", sans-serif;
    font-weight: 700;
    font-size: 19px;
    color: var(--white);
  }
  .agent-phone svg { width: 20px; height: 20px; fill: var(--white); }

  .badges {
    position: absolute;
    left: 28px; top: 255px;
    display: flex;
    gap: 12px;
  }
  .badge { background: #d8d8d8; border-radius: 2px; }
  .badge--housing { width: 82px; height: 18px; }
  .badge--listing { width: 60px; height: 20px; }

  .broker {
    position: absolute;
    left: 206px; top: 208px;
    width: 118px;
    display: flex;
    flex-direction: column;
    align-items: center;
    gap: 8px;
    font-family: "Cinzel", serif;
    font-size: 9px;
    letter-spacing: 0.6px;
    color: #e9e9e9;
    white-space: nowrap;
    text-align: center;
  }
  .broker__mark { width: 44px; height: 44px; border-radius: 50%; background: #d6d6d6; }

  .portrait {
    position: absolute;
    left: 333px; top: 20px;
    width: 261px; height: 328px;
    background: radial-gradient(ellipse at 55% 40%, var(--photo-light) 0%, #8d8d8d 45%, var(--photo-dark) 100%);
  }
</style>
</head>
<body>

  <section class="card card--front">
    <div class="brand">
      <span class="brand__mark"></span>
      <span class="brand__name">Lorena Whitfield</span>
    </div>

    <div class="contact contact--phone">
      <svg viewBox="0 0 24 24" aria-hidden="true"><path d="M6.6 10.8a15.1 15.1 0 0 0 6.6 6.6l2.2-2.2a1 1 0 0 1 1-.25 11.4 11.4 0 0 0 3.6.57 1 1 0 0 1 1 1V20a1 1 0 0 1-1 1A17 17 0 0 1 3 4a1 1 0 0 1 1-1h3.5a1 1 0 0 1 1 1c0 1.25.2 2.46.57 3.6a1 1 0 0 1-.25 1z"/></svg>
      <span>480-555-0137</span>
    </div>

    <div class="contact contact--web">
      <svg viewBox="0 0 24 24" aria-hidden="true"><path d="M2 5h20v14H2z"/><path d="M2 5l10 8 10-8" fill="none" stroke="#fff" stroke-width="1.6"/></svg>
      <span>Lorena@LorenaWhitfieldRE.com</span>
      <span class="contact__spacer"></span>
      <svg viewBox="0 0 24 24" aria-hidden="true"><circle cx="12" cy="12" r="10"/><path d="M2 12h20M12 2c3 3 3 17 0 20M12 2c-3 3-3 17 0 20" fill="none" stroke="#fff" stroke-width="1.4"/></svg>
      <span>LorenaWhitfieldRE.com</span>
    </div>

    <div class="tagline-band">Residential/Commercial Real Estate</div>
  </section>

  <section class="card card--back">
    <div class="brand">
      <span class="brand__mark"></span>
      <span class="brand__name">Lorena Whitfield</span>
    </div>

    <span class="tab"></span>
    <h1 class="agent-name">Lorena Whitfield</h1>
    <p class="agent-title">Realtor/Broker</p>

    <div class="agent-phone">
      <svg viewBox="0 0 24 24" aria-hidden="true"><path d="M6.6 10.8a15.1 15.1 0 0 0 6.6 6.6l2.2-2.2a1 1 0 0 1 1-.25 11.4 11.4 0 0 0 3.6.57 1 1 0 0 1 1 1V20a1 1 0 0 1-1 1A17 17 0 0 1 3 4a1 1 0 0 1 1-1h3.5a1 1 0 0 1 1 1c0 1.25.2 2.46.57 3.6a1 1 0 0 1-.25 1z"/></svg>
      <span>480-555-0137</span>
    </div>

    <div class="badges">
      <span class="badge badge--housing"></span>
      <span class="badge badge--listing"></span>
    </div>

    <div class="broker">
      <span class="broker__mark"></span>
      <span class="broker__name">Harlan Reed Realty</span>
    </div>

    <div class="portrait" role="img" aria-label="Black and white portrait photo of the realtor"></div>

    <div class="tagline-band">Residential/Commercial Real Estate</div>
  </section>

</body>
</html>
```